Web Design Job: Facial Surgery Center (Velmora)--Web Design Needed

We need a web design for Velmora Facial Surgery. Velmora is in Chesterfield, MO (suburb of St. Louis), and is owned by a double board certified facial plastic surgeon and ENT. The website must feature a before and after photo book, a section for patient reviews, drop down menus that outline services offered (one for surgical procedures and one for office/nonsurgical procedures), and "About the Practice" section, a section to talk about the doctor and his staff, a "What's New" section, a section for information for out of town patients, as well as a link to the Medical Spa also owned by the doctor, as well as Facebook and Twitter. We are open to ideas regarding adding a "tour of the surgery center", featuring video footage of the state of the art facility, as well as other video options. We prefer soothing colors such as aquas and blues, light greys, chocolate browns, etc (does not have to follow the color scheme in the attached logo). We would like the design to be easy to digest and informative, but not "thick". It should be an upscale, classy design that will appeal to all age brackets, but especially middle-aged women, as that is the primary clientele.

Target Market(s)

Middle aged women are our most common client, however, younger patients, both male and female, will often visit the site for select procedures.

Industry/Entity Type

Medical

Number of Pages Required

5+ page

Font styles to use
Sans Serif

Colors
86cfc6
85cae6
cee9f5
cfeae6
edf8f6
85acd3
cfdfed

Requirements
Must have
• Before and after picture book, links to Facebook, Twitter and Instagram, a soothing, peaceful aesthetic, a page for reviews, as well as a link to reviews on Yelp or similar page.
Nice to have
• Drop down menus that include the surgical and nonsurgical procedures. Each surgical procedure could have it's own section that includes a before and after picture book.
Should not have
• Too many words!

```html
<!DOCTYPE html>
<html lang="en">
<head>
<meta charset="utf-8">
<title>Velmora Facial Surgery</title>
<link rel="stylesheet" href="https://fonts.googleapis.com/css2?family=Lato:ital,wght@0,400;0,700;1,400&family=Lora&family=Caveat&family=Roboto&display=swap">
<style>
:root{
  --brown:#4d3218;
  --brown-text:#5a3b1e;
  --teal-panel:#1f6a80;
  --logo-blue:#2a6f95;
  --sky:#89d4e6;
  --sky-soft:#e9f5fc;
  --sand:#f2e6d8;
  --nav-active:#7fc6e6;
  --body-blue:#85acd3;
  --btn-grey:#e6e6e6;
  --btn-peach:#fbe3c6;
  --tan:#d6b58a;
  --white:#ffffff;
  --ink:#333333;
}
*{box-sizing:border-box;margin:0;padding:0}
h1,h2,h3{font-weight:400}
html,body{width:669px;height:1200px;overflow:hidden;background:var(--white)}
.canvas{position:relative;width:669px;height:1200px;overflow:hidden;font-family:"Lato",sans-serif}
.layer{position:absolute;left:0;top:0}
/* hero */
.hero-photo{position:absolute;left:0;top:0;width:669px;height:376px;
  background:linear-gradient(180deg,#d3e3ec 0%,#a9c7d5 35%,#6f9fb5 60%,#7a6660 85%,#6b5a56 100%)}
.nav{position:absolute;top:9px;left:222px;display:flex;font-size:4.4px;font-weight:700;color:var(--white);white-space:nowrap}
.nav a{position:absolute;color:inherit;text-decoration:none}
.nav a.is-active{color:var(--nav-active)}
.dropdown{position:absolute;left:304px;top:22px;width:70px;background:var(--white);box-shadow:0 1px 2px rgba(0,0,0,.15)}
.dropdown li{list-style:none;height:17.5px;line-height:17.5px;padding-left:10px;font-size:4.6px;color:#8ea9bb;border-bottom:1px solid #eef2f4;position:relative}
.dropdown li.is-hover{background:#f1f8fb}
.dropdown li::after{content:"›";position:absolute;right:9px;font-size:6px;color:#9aaab5}
.brand{position:absolute;left:86px;top:10px;width:124px;text-align:center;color:var(--logo-blue);font-family:"Lato",sans-serif;font-weight:400}
.brand-name{font-size:12px;letter-spacing:.5px;line-height:12px}
.brand-sub{font-size:3.4px;letter-spacing:2.2px;margin-top:2px}
.call{position:absolute;left:104px;top:62px;color:var(--white)}
.call-label{font-family:"Caveat",cursive;font-size:14px;color:#cfeaf5;line-height:14px}
.call-number{font-family:"Lato",sans-serif;font-size:11.5px;margin-top:2px}
.hero-arrow{position:absolute}
.contact-form{position:absolute;left:270px;top:197px;width:133px;height:179px;background:rgba(86,108,114,.72);border-radius:2px 2px 0 0;padding:5px 0 0 24px}
.form-title{font-family:"Caveat",cursive;font-size:13px;color:#bfe6f2;line-height:13px}
.form-label{display:block;font-family:"Roboto",sans-serif;font-size:8px;color:var(--white);margin-top:4px;line-height:9px;white-space:nowrap}
.form-field{display:block;width:90px;height:9px;background:var(--white);margin-top:1px;border:0}
.form-field.is-message{height:50px}
/* features */
.features{position:absolute;top:425px;left:0;width:669px}
.feature{position:absolute;width:142px;text-align:center}
.feature-icon{width:16px;height:16px;margin:0 auto;border-radius:50%;background:#8cc7e0}
.feature-title{font-family:"Lora",serif;font-weight:400;font-size:9px;letter-spacing:1.4px;color:#7a6453;margin-top:8px;white-space:nowrap}
.feature-title.is-dark{color:var(--brown-text)}
.feature-text{font-size:4.2px;line-height:7px;color:var(--body-blue);margin-top:10px}
.btn{display:inline-block;width:49px;height:14px;line-height:14px;font-size:3.9px;font-weight:700;color:#8aaed0;background:var(--btn-grey);border-radius:1px;margin-top:7px}
.btn.is-hover{background:var(--btn-peach)}
/* lookbook */
.section-title{position:absolute;width:669px;text-align:center;font-family:"Lora",serif;font-weight:400;color:var(--brown-text);letter-spacing:2.4px}
.section-sub{position:absolute;width:669px;text-align:center;font-style:italic;font-size:5.6px;color:#4b3a2c}
.quote-bar{position:absolute;left:140px;top:760px;width:390px;height:16px;
  background:linear-gradient(90deg,rgba(255,255,255,0),rgba(255,255,255,.85) 20%,rgba(255,255,255,.85) 80%,rgba(255,255,255,0));
  text-align:center;font-style:italic;font-size:5.4px;line-height:6.5px;color:#555;padding-top:1.5px}
.quote-mark{color:#e0a96d}
.dots{position:absolute;top:803px;left:314px;display:flex;gap:3px}
.dots span{width:7px;height:7px;border-radius:50%;background:var(--white)}
.dots span.is-active{background:#7fc6e6}
/* video */
.video-card{position:absolute;top:986px;width:177px;height:115px;background:var(--white);border:1px solid #cfcfcf}
.video-badge{position:absolute;left:3px;top:3px;width:14px;height:14px;background:var(--tan)}
.video-title{position:absolute;left:22px;top:4px;font-size:8.5px;font-weight:400;color:var(--ink)}
.video-side{position:absolute;right:3px;top:3px;display:flex;flex-direction:column;gap:1.5px}
.video-side span{width:10px;height:8px;background:#3b3b3b;border-radius:1px}
.video-frame{position:absolute;left:23px;top:17px;width:136px;height:83px}
.video-controls{position:absolute;left:3px;bottom:3px;right:3px;height:9px}
.play{position:absolute;left:0;top:0;width:17px;height:9px;background:#2e2e2e}
.play::after{content:"";position:absolute;left:7px;top:2.3px;border-left:4px solid #fff;border-top:2.2px solid transparent;border-bottom:2.2px solid transparent}
.track{position:absolute;left:20px;right:0;top:0;height:9px;background:#2e2e2e}
.track::before{content:"";position:absolute;left:3px;right:25px;top:4px;height:1.5px;background:#666}
.track::after{content:"";position:absolute;left:3px;width:38px;top:4px;height:1.5px;background:#2ea3dd}
/* footer */
.footer{position:absolute;left:0;top:1180px;width:669px;height:20px;background:var(--brown);color:var(--white);font-size:4.1px}
.footer-copy{position:absolute;left:130px;top:8px}
.footer-links{position:absolute;top:8px;left:0}
.footer-links a{position:absolute;color:inherit;text-decoration:none;white-space:nowrap}
</style>
</head>
<body>
<div class="canvas">

  <!-- hero -->
  <div class="hero-photo" role="img" aria-label="Photo of a bright recovery room with beds, blue curtains, a plant and blue armchairs"></div>

  <svg class="layer" width="669" height="1200" viewBox="0 0 669 1200" aria-hidden="true">
    <path d="M196 0 H669 V24 H214 Q204 22 200 12 Z" fill="var(--brown)"/>
    <path d="M86 0 H210 V118 Q210 121 207 121 H89 Q86 121 86 118 Z" fill="var(--teal-panel)"/>
    <path d="M86 0 H210 V40 Q206 46 188 46 Q130 46 104 26 Q92 14 86 0 Z" fill="var(--white)"/>
    <path d="M0 376 V370 Q120 350 233 359 Q300 364 338 376 Q376 364 443 359 Q556 350 669 370 V376 Z" fill="var(--sky-soft)"/>
    <rect x="0" y="582" width="669" height="303" fill="var(--sand)"/>
    <path d="M0 680 Q120 664 251 659 Q320 660 337 676 Q356 654 420 657 Q560 662 669 680 V854 Q560 830 420 822 Q356 820 337 852 Q322 822 251 822 Q120 830 0 854 Z" fill="var(--sky)"/>
    <line x1="308" y1="628" x2="368" y2="628" stroke="#8fd0cf" stroke-width="1"/>
    <circle cx="338" cy="628" r="1.6" fill="#8fd0cf"/>
    <path d="M0 973 Q120 955 233 950 Q310 950 337 973 Q366 950 443 950 Q556 955 669 973 V1143 Q556 1125 443 1117 Q366 1115 337 1145 Q310 1115 233 1117 Q120 1125 0 1143 Z" fill="var(--sky)"/>
    <line x1="305" y1="927" x2="371" y2="927" stroke="#8fd0cf" stroke-width="1"/>
    <circle cx="338" cy="927" r="1.6" fill="#8fd0cf"/>
    <path d="M100 1180 Q338 1160 576 1180 Z" fill="#8fc7dc"/>
  </svg>

  <div class="brand">
    <div class="brand-name">Velmora</div>
    <div class="brand-sub">FACIAL SURGERY</div>
  </div>

  <div class="call">
    <div class="call-label">Call us</div>
    <div class="call-number">+1 555-014-2290</div>
  </div>

  <nav class="nav">
    <a style="left:0">HOME</a>
    <a style="left:26px">FACIAL PROCEDURES</a>
    <a class="is-active" style="left:81px">OFFICE/NONSURGICAL PROCEDURES</a>
    <a style="left:168px">OUR PRACTICE</a>
    <a style="left:211px">CONTACT INFORMATION</a>
    <a style="left:273px">PHOTO GALLERY</a>
  </nav>

  <ul class="dropdown">
    <li>Procedure 1</li>
    <li class="is-hover">Procedure 2</li>
    <li>Procedure 3</li>
    <li>Procedure 4</li>
    <li>Procedure 5</li>
  </ul>

  <svg class="hero-arrow" style="left:148px;top:176px" width="14" height="22" viewBox="0 0 14 22" aria-label="Previous slide">
    <polyline points="12,1 2,11 12,21" fill="none" stroke="#fff" stroke-width="1"/>
  </svg>
  <svg class="hero-arrow" style="left:546px;top:171px" width="30" height="31" viewBox="0 0 30 31" aria-label="Next slide">
    <rect width="30" height="31" rx="2" fill="#6f95c9" opacity=".85"/>
    <polyline points="11,5 21,15.5 11,26" fill="none" stroke="#fff" stroke-width="1"/>
  </svg>

  <form class="contact-form">
    <div class="form-title">Send a message</div>
    <label class="form-label">YOUR NAME (required)</label>
    <span class="form-field"></span>
    <label class="form-label" style="margin-top:12px">YOUR EMAIL (required)</label>
    <span class="form-field"></span>
    <label class="form-label" style="margin-top:12px">SUBJECT</label>
    <span class="form-field"></span>
    <label class="form-label" style="margin-top:12px">MESSAGE</label>
    <span class="form-field is-message"></span>
  </form>

  <!-- features -->
  <section class="features">
    <div class="feature" style="left:92px">
      <div class="feature-icon" role="img" aria-label="Hand with leaf icon"></div>
      <h2 class="feature-title">ABOUT THE PRACTICE</h2>
      <p class="feature-text">Our practice pairs a double board certified facial plastic surgeon with a caring, experienced staff. We listen first, explain every option clearly, and shape a plan around your goals, comfort and schedule. Every visit is calm, private and unhurried, so you always feel informed, welcome and at ease from first call to final check.</p>
      <span class="btn">LEARN MORE</span>
    </div>
    <div class="feature" style="left:271px">
      <div class="feature-icon" role="img" aria-label="Flower icon"></div>
      <h2 class="feature-title">FACIAL PROCEDURES</h2>
      <p class="feature-text">From eyelid and brow lifts to rhinoplasty and facelift surgery, each procedure is planned with care in our accredited surgery center. Our goal is natural, refreshed results that still look like you, with clear guidance before and after, gentle recovery support and a team that answers every question along the way.</p>
      <span class="btn is-hover">LEARN MORE</span>
    </div>
    <div class="feature" style="left:449px">
      <div class="feature-icon" role="img" aria-label="Sparkle icon"></div>
      <h2 class="feature-title is-dark">OFFICE PROCEDURES</h2>
      <p class="feature-text">Gentle in-office treatments such as injectables, fillers, peels and skin care help you look rested between visits. Most take less than an hour, with little downtime, so you can return to your day. Each plan is tailored to your skin, your budget and your goals, in a calm, private setting.</p>
      <span class="btn">LEARN MORE</span>
    </div>
  </section>

  <!-- lookbook -->
  <h2 class="section-title" style="top:603px;font-size:14px">BEFORE-AFTER LOOKBOOK</h2>
  <p class="section-sub" style="top:637px">results that speak for themselves</p>

  <svg class="layer" style="left:175px;top:654px" width="322" height="200" viewBox="0 0 322 200" role="img" aria-label="Before and after portrait of a patient, shown as an open book">
    <defs>
      <linearGradient id="lookbook-tone" x1="0" y1="0" x2="1" y2="0">
        <stop offset="0" stop-color="#8fd5e6" stop-opacity="0"/>
        <stop offset=".2" stop-color="#9fc8cf"/>
        <stop offset=".5" stop-color="#a7c6c4"/>
        <stop offset=".8" stop-color="#9ccfd9"/>
        <stop offset="1" stop-color="#8fd5e6" stop-opacity="0"/>
      </linearGradient>
    </defs>
    <path d="M0 12 Q80 2 140 6 Q158 10 162 22 Q170 4 200 2 Q260 2 322 12 V168 Q250 166 200 168 Q175 170 162 198 Q150 170 120 168 Q60 166 0 168 Z" fill="url(#lookbook-tone)" opacity=".8"/>
  </svg>

  <div class="quote-bar">
    <span class="quote-mark">”</span> I met with the best specialists.<br>
    I highly recommend them for everyone. <span class="quote-mark">”</span>
  </div>

  <svg class="hero-arrow" style="left:111px;top:760px" width="12" height="16" viewBox="0 0 12 16" aria-label="Previous story">
    <polyline points="10,1 2,8 10,15" fill="none" stroke="#fff" stroke-width="1.6"/>
  </svg>
  <svg class="hero-arrow" style="left:562px;top:761px" width="12" height="16" viewBox="0 0 12 16" aria-label="Next story">
    <polyline points="2,1 10,8 2,15" fill="none" stroke="#fff" stroke-width="1.6"/>
  </svg>

  <div class="dots"><span></span><span></span><span></span><span class="is-active"></span><span></span></div>

  <!-- video -->
  <h2 class="section-title" style="top:903px;font-size:14px">VIDEO FOOTAGE</h2>
  <p class="section-sub" style="top:935px">Check out our latest news</p>

  <article class="video-card" style="left:157px">
    <span class="video-badge"></span>
    <h3 class="video-title">Tour of the surgery center</h3>
    <div class="video-side"><span></span><span></span><span></span></div>
    <div class="video-frame" role="img" aria-label="Video still of the surgery center building exterior"
         style="background:linear-gradient(180deg,#5f8fd0 0%,#a9c8ea 40%,#e4eef3 60%,#b8a892 100%)"></div>
    <div class="video-controls"><span class="play"></span><span class="track"></span></div>
  </article>

  <article class="video-card" style="left:342px">
    <span class="video-badge"></span>
    <h3 class="video-title">Testimonials</h3>
    <div class="video-side"><span></span><span></span><span></span></div>
    <div class="video-frame" role="img" aria-label="Video still of a patient sharing her testimonial"
         style="background:linear-gradient(180deg,#ffffff 0%,#f6efea 45%,#e9d6c8 75%,#7fc3e0 100%);border:1px solid #e2e2e2"></div>
    <div class="video-controls"><span class="play"></span><span class="track"></span></div>
  </article>

  <!-- footer -->
  <footer class="footer">
    <span class="footer-copy">© 2015 Velmora - All Rights Reserved.</span>
    <nav class="footer-links">
      <a style="left:296px">Home</a>
      <a style="left:316px">Facial Procedures</a>
      <a style="left:359px">Office/Nonsurgical Procedures</a>
      <a style="left:425px">Our Practice</a>
      <a style="left:458px">Contact Information</a>
      <a style="left:505px">Photo Gallery</a>
    </nav>
  </footer>

</div>
</body>
</html>
```